Postcard Mailing

Looking to have a design made for postcard, attaching a sample of previous examples and the verbiage we would like used on the new post card. Free to do own design/layout. Same is to show you size and previous mailing card we have done. This post card will be mailed out . Can provide logo for layout directly.

```html
<!DOCTYPE html>
<html lang="en">
<head>
<meta charset="utf-8">
<title>Why HHR – Postcard Samples</title>
<link href="https://fonts.googleapis.com/css2?family=Arimo:wght@400;700&display=swap" rel="stylesheet">
<style>
  :root{
    --sheet:#454545;
    --green:#027c66;
    --gold:#e4d21a;
    --ink:#161616;
    --title-bar:#2e2e2e;
    --panel-grey:#6b6b6b;
    --white:#ffffff;
  }
  *{box-sizing:border-box;margin:0;padding:0}
  html,body{width:887px;height:1200px;overflow:hidden;background:var(--sheet)}
  body{position:relative;font-family:"Arimo",Arial,sans-serif}

  .sample-label{
    position:absolute;left:49px;color:var(--white);font-weight:700;font-size:28px;
    letter-spacing:1px;transform:translate(-50%,-50%) rotate(-90deg);white-space:nowrap;
  }
  .sample-label--one{top:297px}
  .sample-label--two{top:864px}

  .postcard{position:absolute;left:86px;width:736px;overflow:hidden}
  .postcard--green{top:36px;height:523px;background:var(--white)}
  .postcard--grey{top:602px;height:521px;background:var(--white)}

  .photo{position:absolute;left:0;top:0}
  .postcard--green .photo{width:284px;height:490px;
    background:linear-gradient(160deg,#d9c9d6 0%,#8b6a66 35%,#a06f45 55%,#6a3c4a 80%,#7a2a3e 100%)}
  .postcard--grey .photo{width:294px;height:493px;
    background:linear-gradient(160deg,#4b3c7a 0%,#8b6a66 35%,#a06f45 55%,#6a3c4a 80%,#7a2a3e 100%)}

  .shapes{position:absolute;left:0;top:0}

  .info-panel{position:absolute;top:0}
  .postcard--green .info-panel{left:284px;width:452px;height:490px;
    background:linear-gradient(180deg,#ffffff 0%,#eef2f2 55%,#e6ebe8 100%)}
  .postcard--grey .info-panel{left:294px;width:442px;height:493px;background:var(--panel-grey)}

  .bottom-band{position:absolute;left:0;right:0;bottom:0}
  .postcard--green .bottom-band{height:33px;background:var(--green)}
  .postcard--grey .bottom-band{height:28px;background:var(--white)}

  .brand{position:absolute;display:flex;align-items:center;gap:6px;font-weight:700;font-size:12px;letter-spacing:.5px}
  .brand__dot{width:12px;height:12px;border-radius:50%;background:var(--gold)}
  .postcard--green .brand{left:22px;top:44px;color:var(--white)}
  .postcard--grey .brand{left:22px;top:52px;color:var(--green)}

  .headline{position:absolute;text-align:center;font-weight:700;letter-spacing:2px}
  .postcard--green .headline{left:303px;top:59px;width:409px;height:41px;line-height:41px;
    background:var(--title-bar);color:var(--white);font-size:20px}
  .postcard--grey .headline{left:305px;top:28px;width:410px;height:33px;line-height:33px;
    background:var(--white);color:var(--ink);font-size:20px;border-radius:17px}

  .benefits{position:absolute;list-style:none;font-size:11px;letter-spacing:.8px;line-height:21.1px;white-space:nowrap}
  .postcard--green .benefits{left:313px;top:103.5px;color:var(--ink)}
  .postcard--grey .benefits{left:317px;top:70.5px;color:var(--white);font-weight:700}
  .benefits li{position:relative;padding-left:8px}
  .benefits li::before{content:"";position:absolute;left:-4px;top:6.5px;width:8px;height:8px;border-radius:50%}
  .postcard--green .benefits li::before{background:var(--green)}
  .postcard--grey .benefits li::before{background:var(--white)}
  .benefits .sub{padding-left:37px}
  .benefits .sub::before{display:none}

  .plan-bracket{position:absolute;pointer-events:none}
</style>
</head>
<body>

  <div class="sample-label sample-label--one">Sample 1</div>
  <div class="sample-label sample-label--two">Sample 2</div>

  <!-- Green postcard -->
  <section class="postcard postcard--green">
    <div class="photo" role="img" aria-label="Photo of a small wooden model house standing on a patterned rug"></div>
    <div class="info-panel"></div>
    <svg class="shapes" width="736" height="523" viewBox="0 0 736 523" aria-hidden="true">
      <path d="M0 0 H736 V42 H300 C280 42 272 92 240 126 C200 166 110 150 0 160 Z" fill="var(--green)"/>
    </svg>
    <div class="bottom-band"></div>
    <div class="brand"><span class="brand__dot"></span>HARBORLINE HOMES REALTY</div>
    <h1 class="headline">WHY HHR?</h1>
    <svg class="plan-bracket" style="left:0;top:0" width="736" height="523" aria-hidden="true">
      <path d="M313 135 V187 H343 M350 148 H343 V227 H350" fill="none" stroke="var(--green)" stroke-width="2"/>
    </svg>
    <ul class="benefits">
      <li>24/7 caring broker support</li>
      <li>Best agent and team splits in GA</li>
      <li class="sub">100% transaction fee plans starting at $200/transaction</li>
      <li class="sub">100% monthly broker fee plans at $295/month</li>
      <li class="sub">90% agent split with $5,900 cap then 100% (residential only)</li>
      <li class="sub">Several 100% team leader splits available</li>
      <li>16 offices (see HHR website for locations)</li>
      <li>Cutting Edge technology platforms with DealDesk and HHR central</li>
      <li>Award winning LeadNest CRM/Website or AgentHub option</li>
      <li>Passive residual income opportunity</li>
      <li>Licensed Realty School with a 100 seat in-house training center</li>
      <li>Over 100+ free CE classes taught yearly</li>
      <li>No hidden or franchise fees (family owned)</li>
      <li>Luxury, Land, and Commercial divisions</li>
      <li>Member of 16 AGENT BOARD (board membership optional)</li>
      <li>Winner of “Best Workplace in Atlanta” awards</li>
      <li>Mentoring &amp; coaching programs available</li>
      <li>FREE GRCA Access</li>
    </ul>
  </section>

  <!-- Grey postcard -->
  <section class="postcard postcard--grey">
    <div class="photo" role="img" aria-label="Photo of a small wooden model house standing on a patterned rug"></div>
    <div class="info-panel"></div>
    <svg class="shapes" width="736" height="521" viewBox="0 0 736 521" aria-hidden="true">
      <path d="M0 0 H296 C262 86 160 140 0 145 Z" fill="var(--white)"/>
    </svg>
    <div class="bottom-band"></div>
    <div class="brand"><span class="brand__dot"></span>HARBORLINE HOMES REALTY</div>
    <h2 class="headline">WHY HHR?</h2>
    <svg class="plan-bracket" style="left:0;top:0" width="736" height="521" aria-hidden="true">
      <path d="M317 103 V154 H349 M356 115 H349 V194 H356" fill="none" stroke="var(--white)" stroke-width="2"/>
    </svg>
    <ul class="benefits">
      <li>24/7 caring broker support</li>
      <li>Best agent and team splits in GA</li>
      <li class="sub">100% transaction fee plans starting at $200/transaction</li>
      <li class="sub">100% monthly broker fee plans at $295/month</li>
      <li class="sub">90% agent split with $5,900 cap then 100% (residential only)</li>
      <li class="sub">Several 100% team leader splits available</li>
      <li>16 offices (see HHR website for locations)</li>
      <li>Cutting Edge technology platforms with DealDesk and HHR central</li>
      <li>Award winning LeadNest CRM/Website or AgentHub option</li>
      <li>Passive residual income opportunity</li>
      <li>Licensed Realty School with a 100 seat in-house training center</li>
      <li>Over 100+ free CE classes taught yearly</li>
      <li>No hidden or franchise fees (family owned)</li>
      <li>Luxury, Land, and Commercial divisions</li>
      <li>Member of 16 AGENT BOARD (board membership optional)</li>
      <li>Winner of “Best Workplace in Atlanta” awards</li>
      <li>Mentoring &amp; coaching programs available</li>
      <li>FREE GRCA Access</li>
    </ul>
  </section>

</body>
</html>
```